Velmo Online Company needs Trendy Advertising Posters

We need 6 x posters designer:
We have some quotes that we'd like to be designed to be used for online posters, advertising an online business. We need text posters designed for all of the content provided , please send over many designs for us to choose from - each poster will look different from the others. The more examples you provide the better.

Each poster will contain a large, bold, powerful quote - with 'graffiti style' corrections over some words. For example: a vandalised poster with a word replaced with spray paint style font.

Quotes/content and examples provided. The examples we’ve provided are not fixed in terms of colour and layout etc. Creative input would be useful.

Colours/general theme to be similar to: www.velmo.uk

Font styles to use
Serif
Sans Serif
Decorative

Colors
0493ce
33a6d7
85cae6
cee9f5
f9d9e8
eea4c8
e667a6
e34197
0555a3

Requirements
Must have
• Graffiti style font.
Nice to have
• Many designs to choose from.

```html
<!DOCTYPE html>
<html lang="en">
<head>
<meta charset="utf-8">
<title>London Calling – Velmo</title>
<link rel="stylesheet" href="https://fonts.googleapis.com/css2?family=Poppins:wght@900&family=Montserrat:wght@600;800&family=Permanent+Marker&display=swap">
<style>
  :root {
    --bg: #000000;
    --type-fill: #33a6d7;
    --type-edge: #0555a3;
    --type-light: #85cae6;
    --type-pale: #cee9f5;
    --spray: #e34197;
    --spray-soft: #eea4c8;
    --logo: #ffffff;
  }
  html, body {
    margin: 0;
    padding: 0;
    overflow: hidden;
    background: var(--bg);
  }
  .poster {
    position: relative;
    width: 783px;
    height: 1200px;
    background: var(--bg);
    overflow: hidden;
  }
  .quote-line {
    position: absolute;
    margin: 0;
    font-family: "Poppins", sans-serif;
    font-weight: 900;
    font-size: 104px;
    line-height: 1;
    letter-spacing: -1px;
    white-space: nowrap;
    color: var(--type-fill);
    -webkit-text-stroke: 3px var(--type-edge);
    paint-order: stroke fill;
    text-shadow:
      -1px -1px 0 var(--type-light),
      2px 2px 0 var(--type-edge),
      3px 3px 0 var(--type-edge);
    transform: scaleX(0.9);
    transform-origin: left top;
  }
  .quote-line--first { left: 238px; top: 376px; }
  .quote-line--second { left: 36px; top: 494px; }
  .quote-mark {
    position: absolute;
    font-family: "Poppins", sans-serif;
    font-weight: 900;
    font-size: 92px;
    line-height: 1;
    color: var(--type-fill);
    -webkit-text-stroke: 3px var(--type-edge);
    paint-order: stroke fill;
    text-shadow: 2px 2px 0 var(--type-edge);
  }
  .quote-mark--open { left: 176px; top: 370px; }
  .quote-mark--close { left: 700px; top: 486px; }
  .ellipsis-dots {
    position: absolute;
    left: 411px;
    top: 562px;
    display: flex;
    gap: 4px;
  }
  .ellipsis-dots span {
    width: 23px;
    height: 23px;
    border-radius: 50%;
    background: radial-gradient(circle, var(--type-edge) 0 3px, var(--type-fill) 4px 9px, var(--type-light) 10px, var(--type-fill) 11px);
    box-shadow: 1px 1px 0 var(--type-edge);
  }
  .spray-strike {
    position: absolute;
    left: 398px;
    top: 548px;
    width: 300px;
    height: 50px;
  }
  .spray-correction {
    position: absolute;
    left: 560px;
    top: 598px;
    margin: 0;
    font-family: "Permanent Marker", cursive;
    font-size: 60px;
    line-height: 1;
    color: var(--spray);
    text-shadow: 0 0 6px var(--spray-soft);
    transform: rotate(-8deg);
    white-space: nowrap;
  }
  .brand {
    position: absolute;
    left: 0;
    right: 0;
    top: 1080px;
    text-align: center;
    color: var(--logo);
    font-family: "Montserrat", sans-serif;
  }
  .brand-name {
    display: block;
    font-weight: 800;
    font-size: 36px;
    line-height: 1;
    letter-spacing: 0.5px;
  }
  .brand-tagline {
    display: block;
    margin-top: 7px;
    font-weight: 600;
    font-size: 9.5px;
    letter-spacing: 0.3px;
  }
</style>
</head>
<body>
  <main class="poster">
    <span class="quote-mark quote-mark--open" aria-hidden="true">"</span>
    <h1 class="quote-line quote-line--first">London</h1>
    <p class="quote-line quote-line--second">Calling</p>
    <div class="ellipsis-dots" aria-label="ellipsis">
      <span></span><span></span><span></span><span></span><span></span>
      <span></span><span></span><span></span><span></span><span></span>
    </div>
    <svg class="spray-strike" viewBox="0 0 300 50" aria-hidden="true">
      <path d="M6 30 C70 20 150 34 220 22 S280 18 294 24" fill="none" stroke="var(--spray)" stroke-width="9" stroke-linecap="round" opacity="0.92"/>
      <path d="M12 36 C90 28 170 40 286 30" fill="none" stroke="var(--spray-soft)" stroke-width="3" stroke-linecap="round" opacity="0.6"/>
    </svg>
    <span class="quote-mark quote-mark--close" aria-hidden="true">"</span>
    <p class="spray-correction">you!</p>
    <footer class="brand">
      <span class="brand-name">Velmo</span>
      <span class="brand-tagline">REAL ESTATE NETWORK</span>
    </footer>
  </main>
</body>
</html>
```